Book Cover: Memory ashes

Creation of a cover for the book "The Ashes of Memory", 16 x 24 cm. Image available (attached document) Author (top of the cover): "Lucien Dorvalle" Title: "The Ashes of Memory" Other mention: "Preface by Bernard de Montclavel" Publisher (Bottom): "Varnet Editions"

Target Market(s)

General public with interest in Geopolitics

Colors

Designer to choose colors to be used in the design.

Requirements
Must have
• Joined image
Nice to have
• -
Should not have
• -

```html
<!DOCTYPE html>
<html lang="en">
<head>
<meta charset="utf-8">
<title>The Ashes of Memory — Lucien Dorvalle</title>
<link rel="stylesheet" href="https://fonts.googleapis.com/css2?family=Cinzel:wght@500;700&family=Open+Sans:ital,wght@0,600;0,700;1,600&display=swap">
<style>
  :root {
    --backdrop: #d6ebf5;
    --sky-top: #2ccbe6;
    --sky-mid: #4aa9c2;
    --ruins-mid: #5e8fa0;
    --ruins-low: #3d7d90;
    --street: #25596a;
    --band: rgba(232, 246, 251, 0.86);
    --author: #ffffff;
    --title-rose: #d9868c;
    --title-silver: #e4dcdc;
    --title-steel: #d5d7d8;
    --title-shadow: rgba(30, 40, 45, 0.6);
    --preface: #0f4a59;
    --publisher: #f2f8fa;
  }
  * { margin: 0; padding: 0; box-sizing: border-box; }
  html, body {
    width: 1200px; height: 1200px; overflow: hidden;
    background: var(--backdrop);
  }
  .cover {
    position: absolute; left: 234px; top: 55px;
    width: 736px; height: 1105px; overflow: hidden;
    box-shadow: 0 6px 18px rgba(40, 80, 100, 0.25);
  }
  .cover-photo {
    position: absolute; inset: 0;
    background: linear-gradient(180deg, var(--sky-top) 0%, var(--sky-mid) 35%, var(--ruins-mid) 55%, var(--ruins-low) 75%, var(--street) 100%);
  }
  .author {
    position: absolute; top: 64px; left: 0; width: 100%;
    text-align: center;
    font-family: "Open Sans", sans-serif; font-weight: 700;
    font-size: 46px; letter-spacing: -0.5px;
    color: var(--author);
  }
  .title {
    position: absolute; inset: 0;
    font-family: "Cinzel", serif; font-weight: 500;
    text-shadow: 2px 3px 3px var(--title-shadow);
  }
  .title span { position: absolute; line-height: 1; white-space: nowrap; }
  .title .small-top { left: 314px; top: 322px; font-size: 80px; color: var(--title-rose); }
  .title .word-one { left: 120px; top: 392px; font-size: 122px; letter-spacing: 8px; color: var(--title-silver); }
  .title .word-two { left: 200px; top: 506px; font-size: 108px; letter-spacing: -2px; color: var(--title-steel); }
  .title .small-mid { left: 120px; top: 566px; font-size: 48px; color: var(--title-steel); }
  .preface-band {
    position: absolute; left: 0; top: 735px;
    width: 648px; height: 172px;
    background: var(--band);
  }
  .preface {
    position: absolute; left: 0; top: 772px; width: 696px;
    text-align: center;
    font-family: "Open Sans", sans-serif; font-style: italic; font-weight: 600;
    font-size: 35px; line-height: 50px;
    color: var(--preface);
  }
  .publisher {
    position: absolute; left: 0; bottom: 38px; width: 100%;
    text-align: center;
    font-family: "Open Sans", sans-serif; font-weight: 600;
    font-size: 24px; letter-spacing: 1px;
    color: var(--publisher);
  }
</style>
</head>
<body>
  <main class="cover">
    <div class="cover-photo" role="img" aria-label="Teal-toned photograph of a ruined city street with collapsed buildings, rubble and people walking away"></div>
    <p class="author">Lucien Dorvalle</p>
    <h1 class="title">
      <span class="small-top">THE</span>
      <span class="word-one">ASHES</span>
      <span class="small-mid">OF</span>
      <span class="word-two">MEMORY</span>
    </h1>
    <div class="preface-band"></div>
    <p class="preface">Préface de Bernard<br>de Montclavel</p>
    <p class="publisher">Varnet Editions</p>
  </main>
</body>
</html>
```